Zielgruppe
Ich bin Diplom-Psychologe, Psychotherapeut, Coach und Vortragsredner.
In meinen Vorträgen, Seminaren und Coachings sind meine Kunden private Einzelpersonen oder Personen aus Firmen und Unternehmen unterschiedlicher Größe. Mit der Wortmarke 'KARL WENDOLIN - INNER BALANCE & TEAM-TRAINING' ist das Leistungsprofil klar abgegrenzt.
Im Rahmen dessen möchte ich in Abständen Gedankentagebücher herausgeben, welche dazu genutzt werden können, im Coaching, in der Beratung oder im Seminar gewonnene Einsichten und Erkenntnisse festzuhalten. Diese Bücher enthalten neben den dafür nötigen freien Seiten Anregungen in Form von Impulsen, Zitaten und Zeichnungen. Ihre Auftrag ist es, dafür ein passendes Cover zu gestalten.
Aufgabenstellung
BUCHCOVER ERSTELLEN
skalierbare Bilddatei + druckfähiges PDF in sehr guter Auflösung für Buchherstellung
Titel: Säen - Ernten - Teilen
Untertitel: Skizzen- und Wanderheft für Morgenmenschen
Cover - Rückseite - Text
Dieses Skizzen- und Wanderheft für Morgenmenschen möchte gern Sammelort für Ihre Gedanken, Erfahrungen, Erlebnisse und Erkenntnisse sein. Die Seiten werden sich mit der Zeit mit Ihren Texten füllen und so auf einzigartige Weise Ihren Erfahrungsweg dokumentieren. Nichts geht verloren. Sie können immer wieder nachlesen, was Ihnen bisher wichtig war, Ihre Ideen auffrischen und weiterentwickeln. Doch das ist nicht alles. Die im Buch bereits enthaltenen Impulsgedanken, Fragen und Zeichnungen regen Sie zusätzlich zur Selbstreflektion an.
Alles Gute und viel Erfolg!
Auf der Rückseite, im unteren Teil:
Edition KARL WENDOLIN - INNER BALANCE & TEAM-TRAINING
www.karlwendolin-beispiel.de
Dieses Gedankentagebuch soll Menschen in Führungs- und Entscheidungspositionen auf angenehme, wertige, stilvolle Art einladen, als Notiz- und Tagebuch im Arbeits- und Führungsalltag genutzt zu werden. Farben wie weiß, silber, "Merzedesblau", schwarz, dunkles Rot wären meine Favoriten. Doch ich bin für alles offen, wenn es überzeugt.
Es soll beim Sammeln und Sortieren von Ideen und Gedanken helfen. Getreu der Titelunterzeile "Skizzen-und Wanderjournal für Morgenmenschen"
Idealerweise sollen sich Männer und Frauen vom Coverdesign gleichermaßen angesprochen fühlen können. Klar, freundlich, optimistisch, fokussiert, wären noch Attribute, die ich spontan zum Cover nennen kann.
Die Cove..

```html
<!DOCTYPE html>
<html lang="de">
<head>
<meta charset="utf-8">
<title>Säen - Ernten - Teilen – Buchcover</title>
<link rel="stylesheet" href="https://fonts.googleapis.com/css2?family=Ubuntu:wght@300;400;500;700&display=swap">
<style>
  :root {
    --cover-blue: #0a2c7c;
    --frame-line: #3f8fd6;
    --disc-bright: rgba(70, 110, 255, 0.75);
    --disc-mid: rgba(40, 80, 220, 0.45);
    --disc-edge: rgba(20, 50, 160, 0);
    --text-white: #ffffff;
  }
  * { margin: 0; padding: 0; box-sizing: border-box; }
  html, body { width: 1200px; height: 935px; overflow: hidden; background: var(--cover-blue); }
  .cover {
    position: relative;
    width: 1200px; height: 935px;
    background: var(--cover-blue);
    font-family: "Ubuntu", sans-serif;
    color: var(--text-white);
  }
  .trim-frame {
    position: absolute;
    left: 63px; top: 63px; width: 1073px; height: 810px;
    border: 1px solid var(--frame-line);
  }
  .spine-line {
    position: absolute; top: 63px; height: 810px; width: 1px;
    background: var(--frame-line);
  }
  .spine-line--left { left: 576px; }
  .spine-line--right { left: 624px; }

  .disc-field {
    position: absolute;
    background:
      radial-gradient(ellipse 30% 22% at 40% 30%, var(--disc-bright), var(--disc-edge)),
      radial-gradient(ellipse 35% 25% at 60% 65%, var(--disc-mid), var(--disc-edge)),
      radial-gradient(ellipse 60% 50% at 50% 50%, var(--disc-mid), var(--disc-edge));
  }
  .disc-field--back { left: 27px; top: 187px; width: 626px; height: 440px; }
  .disc-field--front { left: 627px; top: 307px; width: 520px; height: 426px; }

  .back-blurb {
    position: absolute; left: 97px; top: 480px; width: 250px;
    font-weight: 700; font-size: 13.6px; line-height: 17.7px;
  }
  .back-blurb p + p { margin-top: 17.7px; }

  .edition {
    position: absolute; left: 97px; top: 796px;
    font-size: 13.6px; line-height: 16px;
  }
  .edition__name, .edition__web { font-weight: 700; }
  .edition__tagline { font-weight: 400; }

  .spine-title, .spine-author {
    position: absolute; left: 600px;
    transform: translateX(-50%);
    writing-mode: vertical-rl;
    white-space: nowrap;
  }
  .spine-title { top: 100px; font-weight: 500; font-size: 28px; letter-spacing: 0.3px; }
  .spine-author { top: 736px; font-weight: 300; font-size: 17px; }

  .front-title {
    position: absolute; left: 737px; top: 100px;
    font-weight: 700; font-size: 58px; line-height: 64px; letter-spacing: 1px;
  }
  .front-subtitle {
    position: absolute; left: 739px; top: 326px;
    font-weight: 700; font-size: 14.5px;
  }
</style>
</head>
<body>
<main class="cover">
  <div class="disc-field disc-field--back" role="img" aria-label="Schwebende blaue Glasscheiben als Illustration"></div>
  <div class="disc-field disc-field--front" role="img" aria-label="Schwebende blaue Glasscheiben als Illustration"></div>

  <div class="trim-frame"></div>
  <div class="spine-line spine-line--left"></div>
  <div class="spine-line spine-line--right"></div>

  <section class="back-blurb">
    <p>Dieses Skizzen- und Wanderheft für Morgenmenschen möchte gern Sammelort für Ihre Gedanken, Erfahrungen, Erlebnisse und Erkenntnisse sein. Die Seiten werden sich mit der Zeit mit Ihren Texten füllen und so auf einzigartige Weise Ihren Erfahrungsweg dokumentieren. Nichts geht verloren. Sie können immer wieder nachlesen, was Ihnen bisher wichtig war, Ihre Ideen auffrischen und weiterentwickeln. Doch das ist nicht alles. Die im Buch bereits enthaltenen Impulsgedanken, Fragen und Zeichnungen regen Sie zusätzlich zur Selbstreflektion an.</p>
    <p>Alles Gute und viel Erfolg!</p>
  </section>

  <footer class="edition">
    <div class="edition__name">Edition Karl Wendolin</div>
    <div class="edition__tagline">Inner Balance &amp; Team-Training</div>
    <div class="edition__web">www.karlwendolin-beispiel.de</div>
  </footer>

  <div class="spine-title">Säen - Ernten - Teilen</div>
  <div class="spine-author">Karl Wendolin</div>

  <h1 class="front-title">Säen<br>Ernten<br>Teilen</h1>
  <p class="front-subtitle">Skizzen- und Wanderheft für Morgenmenschen</p>
</main>
</body>
</html>
```